Women's Day Design for Instagram

Hi there freelancers,

I am looking for a Women's day Design. Main Colour are: Pink, Purple and White.
I have added my own reference but feel free to look at other Women's Day flyers for inspiration.

I have attached a concept/reference image - Reference
Examples of an effect that I want to be use - Example 1 and 2
The main image to use in design - Image for Women's Day Design
Brand Logo - QRT Logo White

Text Instructions

Headline: Celebrating International Women's Day
Date: Saturday, March 7th
Starts: 11am
Location: 41 Corran Rd, Fenbrook Quay, ZN4 7QT (Amber Harbour)
Nearest Train: Fenbrook Quay Linkrail (1 minute walk)
Don't forget to add Logo

Final Size 1080x1350 for instagram

```html
<!DOCTYPE html>
<html lang="en">
<head>
<meta charset="utf-8">
<title>Celebrating International Women's Day</title>
<link rel="stylesheet" href="https://fonts.googleapis.com/css2?family=Great+Vibes&family=Montserrat:wght@600;700;800&display=swap">
<style>
  :root {
    --stage: #4a4a4a;
    --plum-dark: #2a1420;
    --berry: #7c2446;
    --rose: #c4456f;
    --rose-light: #d9668c;
    --crimson: #a8123d;
    --white: #ffffff;
    --silver: #e4e4ea;
    --silver-dark: #a9a9b4;
    --ribbon-text: #b23a63;
  }
  * { margin: 0; padding: 0; box-sizing: border-box; }
  html, body {
    width: 721px; height: 1200px; overflow: hidden;
    background: var(--stage);
  }
  .flyer {
    position: absolute; left: 0; top: 150px;
    width: 721px; height: 901px; overflow: hidden;
    background: linear-gradient(180deg, var(--plum-dark) 0%, #5a2338 22%, var(--rose) 48%, var(--rose-light) 58%, var(--rose) 78%, var(--berry) 100%);
    font-family: "Montserrat", sans-serif;
    color: var(--white);
  }
  .event-photo {
    position: absolute; left: 0; top: 60px; width: 721px; height: 430px;
    background: radial-gradient(ellipse at 50% 45%, rgba(120,70,95,.85) 0%, rgba(90,45,70,.6) 45%, rgba(196,69,111,0) 75%);
  }
  .glitter {
    position: absolute; left: 0; bottom: 0; width: 360px; height: 260px;
    background: radial-gradient(ellipse at 10% 100%, rgba(168,18,61,.85) 0%, rgba(168,18,61,0) 70%);
  }
  .leaf { position: absolute; border-radius: 50% 50% 50% 10%; background: rgba(150,60,95,.55); }
  .leaf--top-left { left: 0; top: 130px; width: 110px; height: 170px; transform: rotate(-20deg); }
  .leaf--right { right: -10px; top: 690px; width: 110px; height: 130px; transform: rotate(30deg); }
  .leaf--bottom { left: 480px; bottom: -30px; width: 90px; height: 60px; }
  .brand {
    position: absolute; top: 52px; width: 100%; height: 40px; line-height: 40px; text-align: center;
    font-weight: 700; font-size: 34px; letter-spacing: 4px; color: var(--white);
  }
  .big-date {
    position: absolute; left: 200px; top: 490px; width: 320px;
    font-weight: 800; font-size: 520px; line-height: 1; text-align: center;
    color: rgba(255,255,255,.28);
  }
  .headline {
    position: absolute; top: 296px; width: 100%; text-align: center;
    font-family: "Great Vibes", cursive; font-weight: 400;
  }
  .headline span {
    display: block;
    background: linear-gradient(180deg, var(--white) 0%, var(--silver) 45%, var(--silver-dark) 70%, var(--white) 100%);
    -webkit-background-clip: text; background-clip: text; color: transparent;
  }
  .headline .line-1 { font-size: 104px; height: 96px; line-height: 96px; }
  .headline .line-2 { font-size: 78px; height: 70px; line-height: 70px; }
  .headline .line-3 { font-size: 102px; height: 110px; line-height: 110px; }
  .details {
    position: absolute; top: 726px; width: 100%; height: 28px; line-height: 28px; text-align: center;
    font-weight: 700; font-size: 18px; letter-spacing: .3px; white-space: nowrap;
  }
  .details .divider { display: inline-block; width: 2px; height: 26px; background: var(--white); vertical-align: middle; margin: 0 16px; }
  .ribbon {
    position: absolute; left: 91px; top: 764px; width: 532px; height: 33px;
    background: var(--white);
    clip-path: polygon(0 0, 100% 0, 97% 50%, 100% 100%, 0 100%, 3% 50%);
    display: flex; align-items: center; justify-content: center;
    font-weight: 800; font-size: 14px; color: var(--ribbon-text); white-space: nowrap;
  }
  .venue {
    position: absolute; top: 806px; width: 100%; height: 22px; line-height: 22px; text-align: center;
    font-weight: 700; font-size: 14.5px; white-space: nowrap;
  }
</style>
</head>
<body>
  <main class="flyer">
    <div class="event-photo" role="img" aria-label="Photo of women seated together on the floor at a community gathering"></div>
    <div class="glitter" role="img" aria-label="Red glitter texture"></div>
    <div class="leaf leaf--top-left" role="img" aria-label="Pink leaf illustration"></div>
    <div class="leaf leaf--right" role="img" aria-label="Pink leaf illustration"></div>
    <div class="leaf leaf--bottom" role="img" aria-label="Pink leaf illustration"></div>

    <div class="brand">QRT</div>
    <div class="big-date" aria-hidden="true">7</div>

    <h1 class="headline">
      <span class="line-1">Celebrating</span>
      <span class="line-2">International</span>
      <span class="line-3">Women's Day</span>
    </h1>

    <p class="details">STARTS: 11AM<span class="divider"></span>DATE: SATURDAY, MARCH 7TH</p>
    <p class="ribbon">NEAREST TRAIN: FENBROOK QUAY LINKRAIL (1 MINUTE WALK)</p>
    <p class="venue">41 CORRAN RD, FENBROOK QUAY, ZN4 7QT (AMBER HARBOUR)</p>
  </main>
</body>
</html>
```